Re-branding for Structural Engineering firm

We need new business cards as part of our current re-branding. We have a new logo (attached), so the card design should incorporate this color scheme. We are a structural engineering firm providing structural building design and seismic consulting services. The final design should communicate professionalism and stability, with a modern look and feel.

```html
<!DOCTYPE html>
<html lang="en">
<head>
<meta charset="utf-8">
<title>Ardent Structural Engineering – Business Card</title>
<link rel="stylesheet" href="https://fonts.googleapis.com/css2?family=Open+Sans:wght@300;400;700&display=swap">
<style>
  :root {
    --backdrop: #1c1d1f;
    --card: #3a3b3e;
    --card-edge: #4a4b4f;
    --tick: #5d5e62;
    --tick-label: #202124;
    --brand-blue: #0a62b3;
    --brand-gray: #6d6e71;
    --text-light: #ffffff;
  }
  html, body {
    margin: 0;
    width: 1200px;
    height: 1200px;
    overflow: hidden;
    background: var(--backdrop);
    font-family: "Open Sans", Arial, sans-serif;
  }
  .card {
    position: absolute;
    left: 75px;
    top: 314px;
    width: 1050px;
    height: 572px;
    border-radius: 28px;
    background: var(--card);
    box-shadow: 0 0 0 2px var(--card-edge) inset;
    overflow: hidden;
  }
  .ruler {
    position: absolute;
    inset: 0;
  }
  .brand {
    position: absolute;
    left: 70px;
    top: 170px;
    width: 270px;
    display: flex;
    align-items: flex-start;
    gap: 14px;
    color: var(--brand-blue);
    font-weight: 700;
  }
  .brand-square {
    width: 22px;
    height: 22px;
    background: var(--brand-blue);
    margin-top: 8px;
    flex: none;
  }
  .brand-name {
    font-size: 34px;
    line-height: 1.1;
    letter-spacing: 1px;
  }
  .brand-name span { display: block; font-size: 20px; letter-spacing: 0.5px; }
  .info-band {
    position: absolute;
    left: 370px;
    top: 196px;
    width: 640px;
    height: 232px;
    background: var(--brand-blue);
    color: var(--text-light);
    box-sizing: border-box;
    padding: 40px 0 0 40px;
  }
  .rule {
    position: absolute;
    left: 370px;
    right: 0;
    height: 6px;
    background: var(--brand-gray);
  }
  .rule.top { top: 180px; }
  .rule.bottom { top: 438px; }
  .person {
    font-size: 30px;
    margin: 0 0 26px;
    font-weight: 700;
    letter-spacing: 0.5px;
  }
  .person .divider { font-weight: 400; margin: 0 10px; }
  .person .role { font-weight: 300; font-size: 24px; letter-spacing: 0.3px; }
  .contact {
    font-size: 22px;
    font-weight: 400;
    margin: 0 0 8px;
  }
  .contact .divider { margin: 0 8px; }
</style>
</head>
<body>
  <div class="card">
    <svg class="ruler" width="1050" height="572" viewBox="0 0 1050 572" aria-hidden="true">
      <defs>
        <pattern id="minor-top" width="9.5" height="20" patternUnits="userSpaceOnUse">
          <line x1="1" y1="0" x2="1" y2="14" stroke="var(--tick)" stroke-width="1.5"/>
        </pattern>
        <pattern id="minor-bottom" width="9.5" height="20" patternUnits="userSpaceOnUse" y="552">
          <line x1="1" y1="6" x2="1" y2="20" stroke="var(--tick)" stroke-width="1.5"/>
        </pattern>
        <pattern id="major-top" width="47.5" height="30" patternUnits="userSpaceOnUse">
          <line x1="1" y1="0" x2="1" y2="26" stroke="var(--tick)" stroke-width="2"/>
        </pattern>
        <pattern id="major-bottom" width="47.5" height="30" patternUnits="userSpaceOnUse" y="542">
          <line x1="1" y1="4" x2="1" y2="30" stroke="var(--tick)" stroke-width="2"/>
        </pattern>
      </defs>
      <rect x="30" y="0" width="990" height="20" fill="url(#minor-top)"/>
      <rect x="30" y="0" width="990" height="30" fill="url(#major-top)"/>
      <rect x="30" y="552" width="990" height="20" fill="url(#minor-bottom)"/>
      <rect x="30" y="542" width="990" height="30" fill="url(#major-bottom)"/>
      <g fill="var(--tick-label)" font-family="Open Sans, Arial, sans-serif" font-size="15">
        <text x="40" y="530">1</text>
        <text x="230" y="530">2</text>
        <text x="420" y="530">3</text>
        <text x="610" y="530">4</text>
        <text x="800" y="530">5</text>
        <g transform="rotate(180 525 50)">
          <text x="40" y="56">1</text>
          <text x="230" y="56">2</text>
          <text x="420" y="56">3</text>
          <text x="610" y="56">4</text>
          <text x="800" y="56">5</text>
        </g>
      </g>
    </svg>

    <div class="brand">
      <div class="brand-square"></div>
      <div class="brand-name">ARDENT<span>STRUCTURAL</span><span>ENGINEERING</span></div>
    </div>

    <div class="rule top"></div>
    <div class="info-band">
      <p class="person">MARCUS HALE<span class="divider">|</span><span class="role">Director</span></p>
      <p class="contact">555.214.3080<span class="divider">|</span>info@ardentse.com<span class="divider">|</span>www.ardentse.com</p>
      <p class="contact">4410 Granite Ridge Rd. Ste.210, Oakvale, California 90417</p>
    </div>
    <div class="rule bottom"></div>
  </div>
</body>
</html>
```